The Iron Trials Borinquen Coast (ITBC) – Sponsorship Proposal 2026 | Second Edition

We are looking to redesign and elevate our Sponsorship Proposal for the second edition of The Iron Trials Borinquen Coast (ITBC) - a Tactical Fitness competition that combines functional fitness and live-fire shooting in a safe and controlled environment.
The first edition (March 7, 2026) was a proven success, and the updated proposal must reflect that evolution from concept to validated event.
OBJECTIVE
Create a visually striking, premium, and highly structured sponsorship proposal that communicates:
- Credibility (proven event)
- Growth (scaling momentum)
- Experience (not just competition, but a full event)
----------------------------
KEY DATA TO INCLUDE (VERY IMPORTANT)
The design must highlight the following real metrics prominently:
- 96 registered athletes
- 240+ spectators
- 35 volunteers
- 370+ total attendees
- 14 female athletes
- 5 youth participants (ages 12–16)
- $3,300 awarded in prize money
INAUGURAL SPONSORS:
- Coastal Sky Corps
- Caribe Territorial Defense Reserve
- Harbor Militia Auxiliary
- Crestmoor Real Estate
- MTK (Mariposa Trek Kit)
- Quillstone Studio
- Reef Motion 442, KORVA San Juan
- Premier Dispatch PR
- Core Harmony
NEXT EVENT (IMPORTANT FOR DESIGN STORY)
- Event Date: December 19, 2026
- Expected Attendance:
- 130+ athletes
- 300+ spectators
- ~500 total attendees
- Theme: Christmas Experience
- Full event decorated in Christmas theme
- Food vendors + traditional Puerto Rican roasted pork (150+ lbs), community, and sponsor activations
👉 This is NOT just a competition - it is an experience-driven event.
STRUCTURE (BASED ON CURRENT PROPOSAL)
- Use the existing proposal as structural reference , but improve layout, hierarchy, and storytelling:
- Cover Page (modern + bold)
- Executive Summary (UPDATED with real results)
- Event Concept / Experience
- Audience & Attendance (with real + projected numbers)
- Sponsors (social proof section)
- Sponsorship Packages (Alpha = $10,000, Bravo = $1,000, Charlie = $500, Delta = $250)
- Why Sponsor ITBC
- Contact Page
EVENT DIVISIONS (UPDATED – VERY IMPORTANT)
The proposal must clearly showcase the five official competition divisions, with strong visual hierarchy (icons, images, or cards per division). This section should feel dynamic, premium, and easy to scan.
Divisions to include:
SCALE DIVISION (Adaptive)
An adaptive division for those who want to experience ITBC in a controlled environment.
No rankings. No prizes.
This is about completing the challenge.
BEGINNER DIVISION
For athletes ready to compete in a structured and approachable format.
Challenging, but accessible.
Athletes compete for placement.
INTERMEDIATE DIVISION
For athletes with a strong foundation in fitness and shooting.
Heavier loads. Higher standards.
Performance matters.
JÍBARO DIVISION (Elite)
The highest level of competition at ITBC.
Retention holsters required. Rifles carried in slings. Heavier loads.
Built for athletes who want to prove themselves.
MASTERS 45+ DIVISION
For athletes 45+ who want to compete while prioritizing longevity and control.
Maintains competitive intensity within an age-based category.
2-GUN FORMAT (IMPORTANT – INCLUDE BELOW DIVISIONS)
All divisions are available in either:
Pistol
2-Gun (Pistol + Rifle)
In the 2-Gun format, athletes utilize both pistol and rifle throughout the competition, transitioning between weapons under physical fatigue and time pressure.
DESIGN NOTE FOR THIS SECTION
Present divisions as individual visual blocks/cards (like the reference provided)
Use bold titles + short descriptions (keep text tight)
Include action images per division if possible
Highlight Jíbaro Division as the elite tier visually
Ensure this section is one of the most visually engaging pages in the proposal
DESIGN STYLE & VISUAL DIRECTION
We want a military / tactical / premium fitness aesthetic, similar to brands like:
- Brindle Athletics
- The Valor Circuit
- MeshLift-style event decks
Tone:
- Strong
- Clean
- Masculine but modern
- Minimal clutter
COLOR PALETTE (MANDATORY)
Use the following brand colors:
- Light Olive Green (#636B2F)
- Dark Olive Green (#3D4127)
- Sand / Khaki (#C2B280)
- Charcoal / Black (#1C1C1C)
- Light Gray (#D3D3D3)
- White (#FFFFFF)
- Accent Red (#C80018) – for highlights only
DESIGN NOTES
- Use bold typography (military/tactical feel - I will include the font called BOOTCAMP which is the main font used for the first edition)
- Strong use of contrast (dark backgrounds + light text)
- Icons for stats (athletes, spectators, etc.)
- Clean infographics for numbers
- Full-page images for impact (action shots, athletes, shooting, fitness)
- Official logo included (PNG and vectorized)
- Keep it visually dynamic but easy to read
IMPORTANT MESSAGE SHIFT
The proposal must clearly communicate:
- This is NOT a new event
- This is a proven concept that is scaling
Before: “Support us”
Now: “Join a growing movement early”
FINAL DELIVERABLE
- Print-ready PDF (high quality)
- Editable source file (Illustrator)
- Modern, clean layout with strong visual hierarchy
Website: www.theitbc-example.com
Instagram: https://www.instagram.com/theitbc_demo/
- BOOTCAMP

```html
<!DOCTYPE html>
<html lang="en">
<head>
<meta charset="utf-8">
<title>ITBC Sponsorship Proposal</title>
<link rel="stylesheet" href="https://fonts.googleapis.com/css2?family=Teko:wght@500;600&family=Montserrat:wght@400;500;600&display=swap">
<style>
:root{
  --olive:#636B2F; --olive-dark:#3D4127; --olive-band:#4B5231;
  --sand:#C2B280; --charcoal:#1C1C1C; --panel:#272725; --gray:#D3D3D3;
  --white:#FFFFFF; --red:#C80018; --canvas:#E2E2E2;
}
*{box-sizing:border-box;margin:0;padding:0}
html,body{width:953px;height:1200px;overflow:hidden;background:var(--canvas)}
body{position:relative;font-family:"Montserrat",sans-serif;color:var(--white)}
.head{font-family:"Teko",sans-serif;font-weight:500;color:var(--sand);line-height:.9;letter-spacing:.3px;text-transform:uppercase}
.page{position:absolute;width:295px;height:382px;background:var(--panel);overflow:hidden}
.p1{left:32px;top:25px}.p2{left:328px;top:25px}.p3{left:625px;top:25px}
.p4{left:32px;top:408px}.p5{left:328px;top:408px}.p6{left:625px;top:408px}
.p7{left:328px;top:791px}
.abs{position:absolute}
.photo{position:absolute}
.band{position:absolute;left:0;top:0;bottom:0;width:29px;background:var(--olive-band)}
.body{font-size:5.4px;line-height:1.62;color:var(--gray);text-align:justify}
.title{position:absolute;left:0;right:0;text-align:center;font-size:19px}

/* cover */
.cover-photo{inset:0;background:linear-gradient(160deg,#4d5a3a 0%,#2f3a2c 40%,#3a4a5a 70%,#1c1c1c 100%)}
.cover-top{position:absolute;left:0;right:0;top:0;height:40px;background:var(--charcoal)}
.cover-seal{position:absolute;left:112px;top:14px;width:72px;height:72px;border-radius:50%;background:var(--charcoal);border:2px solid var(--white);display:flex;align-items:center;justify-content:center;font-family:"Teko",sans-serif;font-size:20px;color:var(--white)}
.cover-title{position:absolute;left:73px;top:150px;font-family:"Teko",sans-serif;font-weight:600;font-size:32px;line-height:.86;color:var(--white)}
.cover-frame{position:absolute;left:10px;right:8px;top:305px;height:77px;background:#141414;border:3px solid #6b5a44;border-bottom:none;border-radius:4px 4px 0 0;text-align:center}
.cover-frame .head{color:var(--white);font-size:28px;margin-top:6px}
.cover-frame p{font-size:9px;font-weight:500;line-height:1.3}

/* divisions */
.div-tag{position:absolute;left:73px;top:14px;width:206px;height:16px;background:var(--olive-band);font-size:5.2px;color:var(--sand);display:flex;align-items:center;justify-content:center}
.division{position:absolute;left:73px;width:210px;height:46px}
.division .thumb{position:absolute;left:0;top:0;width:60px;height:46px;background:linear-gradient(135deg,#5a5f48,#2e3024)}
.division .head{position:absolute;left:64px;top:0;font-size:13px}
.division p{position:absolute;left:64px;top:15px;right:0;font-size:4.9px;line-height:1.6;color:var(--gray);text-align:justify}
.division.elite .head{color:var(--sand)}
.twogun{position:absolute;left:73px;top:314px;width:210px;height:58px;background:var(--olive-band)}
.twogun .thumb{position:absolute;left:0;top:0;width:56px;height:58px;background:var(--olive)}
.twogun p{position:absolute;left:70px;right:6px;font-size:4.9px;line-height:1.6;color:var(--gray);text-align:justify}

/* location */
.map{left:9px;top:92px;width:278px;height:117px;background:linear-gradient(135deg,#3f5a35,#5e6b52 45%,#2d4229);border:1px solid #3aa0d8}
.gps{position:absolute;left:0;right:0;top:236px;text-align:center}
.gps .head{color:var(--white);font-size:12px}
.gps .coord{font-family:"Teko",sans-serif;font-size:7.5px;line-height:1;color:var(--white)}
.note-box{position:absolute;left:38px;right:10px;top:290px;height:39px;background:var(--olive-band);padding:5px 6px;font-size:5.4px;line-height:1.6;color:var(--gray)}

/* audience */
.stats{position:absolute;left:40px;top:89px;display:flex;gap:4px}
.stat{width:32px;text-align:center}
.stat .icon{width:32px;height:39px;background:var(--sand);border-radius:2px}
.stat .num{font-family:"Teko",sans-serif;font-size:16px;line-height:1;margin-top:3px;color:var(--white)}
.stat .lbl{font-size:3px;font-weight:600;line-height:1.3;text-transform:uppercase}
.trusted{position:absolute;left:118px;top:269px;width:87px;height:16px;background:var(--olive-band);font-size:5.4px;color:var(--gray);display:flex;align-items:center;justify-content:center}
.sponsors{position:absolute;left:40px;right:10px;top:299px;display:flex;flex-wrap:wrap;justify-content:center;gap:6px 9px}
.sponsor{font-size:5.5px;font-weight:600;color:var(--white);display:flex;align-items:center;gap:3px}
.sponsor i{width:8px;height:8px;background:var(--sand);display:inline-block}
.sponsor i.round{border-radius:50%}

/* packages */
.pkg-band{position:absolute;left:0;right:0;top:17px;height:27px;background:var(--olive-band);text-align:center}
.pkg-band .head{font-size:19px;padding-top:4px}
.plate{position:absolute;background:#121212;border:3px solid #5b5248;border-radius:5px;text-align:center}
.plate .head{color:var(--gray)}
.alpha{left:59px;top:50px;width:175px;height:84px}
.alpha .big{font-size:28px;margin-top:5px}
.alpha .mid{font-size:15px}
.alpha .small{font-size:6px;line-height:1.1;padding:1px 6px 0}
.tier{top:142px;width:61px;height:83px}
.tier .name{font-size:16px;margin-top:4px}
.tier .price{font-size:16px}
.tier .avail{font-size:6px;color:var(--white)}
.tier p{font-size:3.4px;line-height:1.35;color:var(--gray);padding:1px 4px 0}
.inkind{position:absolute;left:20px;top:232px;width:255px;height:61px;background:var(--sand);border-radius:4px;color:var(--charcoal)}
.inkind .head{position:absolute;left:10px;top:7px;color:var(--olive-dark);font-size:14px;line-height:.82}
.inkind .head small{font-size:9px;display:block;margin-top:2px}
.inkind .rule{position:absolute;left:100px;top:6px;bottom:6px;width:1px;background:var(--olive-dark)}
.inkind ul{position:absolute;left:105px;right:6px;top:6px;font-size:4.1px;line-height:1.55;list-style:none}
.why{position:absolute;left:10px;right:10px;top:320px;height:42px;background:var(--olive-band);padding:4px 6px;font-size:5.4px;line-height:1.6;color:var(--gray)}

/* closing */
.closing-frame{position:absolute;left:38px;top:9px;width:247px;height:206px;background:#111;border:5px solid #5e4d3a;border-radius:6px;text-align:center}
.closing-frame .head{color:var(--white)}
.cal{width:14px;height:13px;margin:10px auto 0}
.expect{display:flex;justify-content:center;margin-top:4px}
.expect .col{width:52px;padding:0 2px;border-left:1px solid #777}
.expect .col:first-child{border-left:none}
.expect .ico{height:26px;margin:0 6px;background:var(--sand);opacity:.85;border-radius:2px}
.expect .head{font-size:8.5px;margin-top:3px;line-height:.95}
.closing-list{text-align:left;margin:10px 0 0 28px;list-style:none}
.closing-list li{font-family:"Teko",sans-serif;font-size:8.5px;line-height:1.15;color:var(--white);position:relative;padding-left:10px}
.closing-list li:before{content:"";position:absolute;left:0;top:3px;width:3px;height:3px;border-radius:50%;background:var(--white)}
.contact{position:absolute;left:29px;right:0;top:226px;height:78px;background:var(--olive-band);text-align:center}
.contact .head{font-size:17px;margin-top:4px;border-bottom:1px solid var(--sand);display:inline-block}
.contact .name{color:var(--white);font-size:13px;margin-top:2px}
.contact p{font-size:6.8px;font-weight:500;line-height:1.6}
.closing-photo{left:29px;right:0;top:304px;height:56px;background:linear-gradient(180deg,#3a3f38,#5a5e52 60%,#2b2b2b)}
.closing-banner{position:absolute;left:29px;right:0;top:360px;height:22px;background:var(--sand);text-align:center}
.closing-banner .head{color:var(--charcoal);font-size:17px;padding-top:2px}
</style>
</head>
<body>

<!-- Cover -->
<section class="page p1">
  <div class="photo cover-photo" role="img" aria-label="Athlete in ear protection and sunglasses aiming a scoped rifle outdoors"></div>
  <div class="cover-top"></div>
  <div class="cover-seal">ITBC</div>
  <h1 class="cover-title">THE IRON<br>TRIALS BORINQUEN<br>COAST<br>(ITBC)</h1>
  <div class="cover-frame">
    <div class="head">Sponsorship Proposal</div>
    <p>December 19, 2026<br>Ridgeline Range Club – Aguas Buenas, Puerto Rico</p>
  </div>
</section>

<!-- About -->
<section class="page p2">
  <div class="band"></div>
  <h2 class="title head" style="top:22px;font-size:18px;left:29px">The Iron Trials<br>Borinquen Coast (ITBC)</h2>
  <p class="body abs" style="left:40px;right:12px;top:76px">ITBC is the Caribbean's original functional fitness and live-fire competition—an unmatched, one-of-a-kind event where strength, precision, and adrenaline converge. Designed as a high-intensity experience, ITBC brings together athletes, competitive shooters, tactical professionals, and performance-driven enthusiasts in a single arena where physical endurance and mental sharpness are tested equally. Over the course of one action-packed day, participants take on a series of demanding challenges that combine functional training, speed, decision-making, marksmanship, and resilience under pressure. Every stage is built to push competitors beyond their comfort zone, creating an electrifying environment that celebrates discipline, focus, and elite performance while delivering a spectacle unlike anything else in the Caribbean.</p>
  <div class="photo" style="left:0;right:0;top:185px;bottom:0;background:linear-gradient(100deg,#4b4f3e,#6a6a5c 35%,#3d4233 65%,#57604a)" role="img" aria-label="Collage of athletes sprinting and shooting pistols during competition stages"></div>
</section>

<!-- Divisions -->
<section class="page p3">
  <div class="photo" style="left:0;top:0;bottom:0;width:73px;background:linear-gradient(180deg,#3d4a30,#2c2c2a 50%,#4a4636)" role="img" aria-label="Competitor in cap and sport sunglasses standing on the range"></div>
  <div class="div-tag">The competition is organized into divisions designed for every level</div>
  <div class="division" style="top:37px"><div class="thumb" role="img" aria-label="Adaptive division athletes on course"></div><div class="head">Scale Division (Adaptive)</div><p>An adaptive division for those who want to experience ITBC in a controlled environment. No rankings. No prizes. This is about completing the challenge.</p></div>
  <div class="division" style="top:92px"><div class="thumb" role="img" aria-label="Beginner athlete carrying a load"></div><div class="head">Beginner Division</div><p style="top:20px">For athletes ready to compete in a structured and approachable format. Challenging, but accessible. Athletes compete for placement.</p></div>
  <div class="division" style="top:147px"><div class="thumb" role="img" aria-label="Intermediate athlete firing a pistol"></div><div class="head">Intermediate Division</div><p style="top:20px">For athletes with a strong foundation in fitness and shooting. Heavier loads. Higher standards. Performance matters.</p></div>
  <div class="division elite" style="top:202px"><div class="thumb" role="img" aria-label="Jíbaro division athletes shooting prone"></div><div class="head">Jíbaro Division</div><p style="top:20px">The highest level of competition at ITBC. Retention holsters required. Rifles carried in slings. Heavier loads. Built for athletes who want to prove themselves.</p></div>
  <div class="division" style="top:257px"><div class="thumb" role="img" aria-label="Masters athlete aiming a rifle"></div><div class="head">Masters 45+ Division</div><p style="top:20px">For athletes 45+ who want to compete while prioritizing longevity and control. Maintains competitive intensity within an age-based category.</p></div>
  <div class="twogun">
    <div class="thumb" role="img" aria-label="Pistol and rifle silhouettes"></div>
    <p style="top:3px">All divisions are available in either: Pistol / 2-Gun (Pistol + Rifle)</p>
    <p style="top:20px">In the 2-Gun format, athletes utilize both pistol and rifle throughout the competition, transitioning between weapons under physical fatigue and time pressure.</p>
  </div>
</section>

<!-- Location -->
<section class="page p4">
  <div class="band"></div>
  <h2 class="title head" style="top:20px;left:29px">Event Location</h2>
  <p class="body abs" style="left:39px;right:10px;top:47px">Ridgeline Range Club, Aguas Buenas, Puerto Rico. The club spans 172 acres, offering exclusive use of the grounds for The Iron Trials Borinquen Coast. The event will occupy the newly leveled field (~90m × 29m) and surrounding trails for running/ruck stages, creating a safe and controlled setting for both physical and shooting challenges.</p>
  <div class="photo map" role="img" aria-label="Aerial site map marking the competition zone, spectators zone and sponsorship village with available and unavailable spaces"></div>
  <svg class="abs" style="left:138px;top:220px" width="100" height="62" viewBox="0 0 100 62" aria-hidden="true">
    <path d="M50 0 L45 8 H55Z M50 62 L45 54 H55Z M0 31 L9 26 V36Z M100 31 L91 26 V36Z" fill="#636B2F"/>
  </svg>
  <div class="gps" style="top:235px"><div class="head">GPS Coordinates</div><div class="coord">18.240000000000000,<br>-66.080000000000000</div></div>
  <div class="note-box">The event area includes the Competition Zone, Spectator Area, Sponsor &amp; Concessions Village, Testing &amp; Prep Field, and Athlete Warm-up Zone, covering 14,537 square meters. The running/ruck course extends over 920 meters, integrated into the site's natural terrain.</div>
  <p class="abs" style="left:59px;right:22px;top:339px;font-size:5.4px;line-height:1.6;color:var(--gray)">In essence, sponsors and participants will have full access to the property, transforming it into a stage dedicated to athletic performance, tactical excellence, and brand activation.</p>
</section>

<!-- Audience -->
<section class="page p5">
  <div class="band"></div>
  <h2 class="title head" style="top:20px;left:29px">Audience and Attendance</h2>
  <p class="body abs" style="left:44px;right:14px;top:47px;text-align:left">The Iron Trials Borinquen Coast (ITBC) attracts a highly concentrated audience of active, motivated adults with strong purchasing power and high brand loyalty to companies that support their performance-driven lifestyle.</p>
  <div class="stats">
    <div class="stat"><div class="icon" role="img" aria-label="Runner icon"></div><div class="num">96</div><div class="lbl">Registered athletes</div></div>
    <div class="stat"><div class="icon" role="img" aria-label="Crowd icon"></div><div class="num">240+</div><div class="lbl">Spectators</div></div>
    <div class="stat"><div class="icon" role="img" aria-label="Helping hands icon"></div><div class="num">35</div><div class="lbl">Volunteers</div></div>
    <div class="stat"><div class="icon" role="img" aria-label="Large group icon"></div><div class="num">370+</div><div class="lbl">Total attendees</div></div>
    <div class="stat"><div class="icon" role="img" aria-label="Female runner icon"></div><div class="num">14</div><div class="lbl">Female athletes</div></div>
    <div class="stat"><div class="icon" role="img" aria-label="Youth icon"></div><div class="num">5</div><div class="lbl">Youth participants (ages 12–16)</div></div>
    <div class="stat"><div class="icon" role="img" aria-label="Dollar sign icon"></div><div class="num">$3,300</div><div class="lbl">Awarded in prize money</div></div>
  </div>
  <p class="body abs" style="left:44px;right:14px;top:172px">The core demographic is ages 25–44, with additional participation from 18–24 and 45–55, and consists largely of mid- to high-income professionals (typical household income mid-$40K to $90K+) working in technology, engineering, aviation, healthcare, emergency services, law enforcement, military, security, and business leadership roles. This audience regularly invests in gym memberships, coaching, supplements, outdoor and tactical gear, firearms, and training, and is known for high brand loyalty and early adoption of performance equipment, tactical apparel, and fitness technology – making ITBC an ideal platform for sponsors seeking direct engagement with disciplined, ambitious consumers, first responders y veterans.</p>
  <div class="trusted">Trusted by these sponsors</div>
  <div class="sponsors">
    <span class="sponsor">Coastal Sky Corps</span>
    <span class="sponsor"><i></i>Caribe Territorial Defense Reserve</span>
    <span class="sponsor">MTK</span>
    <span class="sponsor"><i class="round"></i>Harbor Militia Auxiliary</span>
    <span class="sponsor">Crestmoor Real Estate</span>
    <span class="sponsor">KORVA San Juan</span>
    <span class="sponsor">Premier Dispatch PR</span>
    <span class="sponsor"><i class="round"></i>Core Harmony</span>
    <span class="sponsor">Quillstone Studio</span>
  </div>
</section>

<!-- Packages -->
<section class="page p6">
  <div class="pkg-band"><h2 class="head">Sponsorship Packages</h2></div>
  <div class="plate alpha">
    <div class="head big">Alpha / $10,000</div>
    <div class="head mid">Main Sponsor – 1 Available</div>
    <div class="head small">The premier sponsorship tier. Full brand integration across the entire event, including naming presence in key locations and all major advertising.</div>
  </div>
  <div class="plate tier" style="left:37px"><div class="head name">Bravo</div><div class="head price">$1,000</div><div class="head avail">Up to 3 available</div><p>Offers solid brand visibility and opportunities for active participation.</p></div>
  <div class="plate tier" style="left:117px"><div class="head name">Charlie</div><div class="head price">$500</div><div class="head avail">Up to 20 available</div><p>Designed for brands seeking event presence and digital promotion at an accessible level.</p></div>
  <div class="plate tier" style="left:196px"><div class="head name">Delta</div><div class="head price">$250</div><div class="head avail">Unlimited</div><p>Ideal for businesses seeking local and digital visibility while supporting the event.</p></div>
  <div class="inkind">
    <div class="head">In-Kind<br>Sponsorships<small>Product or Service<br>Donations</small></div>
    <div class="rule"></div>
    <ul>
      <li>We welcome in-kind contributions that enhance the event experience or operations.</li>
      <li>• Hydration and nutrition (beverages, snacks, supplements).</li>
      <li>• Equipment and accessories (targets, uniforms, gym gear).</li>
      <li>• Media, printing, or logistics services.</li>
      <li>• Transportation, photography, or volunteer support.</li>
    </ul>
  </div>
  <h2 class="title head" style="top:300px;font-size:17px">Why Invest in ITBC</h2>
  <div class="why">ITBC gives sponsors direct access to a highly engaged, performance-driven community. By blending functional fitness, endurance, and tactical precision, it offers brands an authentic way to connect with athletes, veterans, first responders, and ambitious professionals while building visibility, credibility, and long-term loyalty in a fast-growing market.</div>
</section>

<!-- Closing -->
<section class="page p7">
  <div class="band"></div>
  <div class="closing-frame">
    <svg class="cal" viewBox="0 0 14 13" aria-hidden="true"><rect x="1" y="2" width="12" height="10" fill="none" stroke="#fff" stroke-width="1"/><path d="M1 5H13M4 0V3M10 0V3" stroke="#fff"/><path d="M3 7h2M6 7h2M9 7h2M3 9.5h2M6 9.5h2M9 9.5h2" stroke="#fff"/></svg>
    <div class="head" style="font-size:14px;margin-top:3px">December 19, 2026</div>
    <div class="head" style="font-size:14px;margin-top:4px">Expected Attendance</div>
    <div class="expect">
      <div class="col"><div class="ico" role="img" aria-label="Runner icon"></div><div class="head">130+ Athletes</div></div>
      <div class="col"><div class="ico" role="img" aria-label="Crowd icon"></div><div class="head">300+<br>Spectators</div></div>
      <div class="col"><div class="ico" role="img" aria-label="Large group icon"></div><div class="head">500 Total<br>Attendees</div></div>
      <div class="col"><div class="ico" role="img" aria-label="Christmas ornaments icon"></div><div class="head">Theme:<br>Christmas<br>Experience</div></div>
    </div>
    <ul class="closing-list">
      <li>FULL EVENT DECORATED IN CHRISTMAS THEME</li>
      <li>FOOD VENDORS + TRADITIONAL PUERTO RICAN ROASTED PORK<br>(150+ LBS), COMMUNITY, AND SPONSOR ACTIVATIONS</li>
    </ul>
  </div>
  <div class="contact">
    <div class="head">Contac</div>
    <div class="head name">Marco A. Vélez</div>
    <p>The Iron Trials Borinquen Coast (ITBC), Founder &amp; CEO<br>marco@theitbc-example.com | 787-555-0142 | www.instagram.com/theitbc_demo<br>PO BOX 550123 | San Juan, PR 00999</p>
  </div>
  <div class="photo closing-photo" role="img" aria-label="Close-up of a competitor aiming a rifle"></div>
  <div class="closing-banner"><div class="head">Join a Growing Movement Early</div></div>
</section>

</body>
</html>
```